Stationary Package
Business Card / Letterhead / Envelop
I need double sided standard sized Business Card [3.5" x 2"]
use same look and feel font(s)
Professional
Daniel Whitfield
Marketing Strategist
4518 Harwick Crescent
Mississauga, Ontario, L4T 3K8
danielwhitfield@vellorahaus.com
www.vellorahaus.com
design package for the marketing industry
Logo with tag line
plus the website address
Logo and Tag Line
eps logo
pdf logo version

```html
<!DOCTYPE html>
<html lang="en">
<head>
<meta charset="utf-8">
<title>Daniel Whitfield Stationery</title>
<link rel="stylesheet" href="https://fonts.googleapis.com/css2?family=Montserrat:wght@400;600;700&family=Open+Sans:wght@400;600&display=swap">
<style>
  :root{
    --bg:#e9ebef;
    --paper:#ffffff;
    --blue:#1f4fd1;
    --blue-light:#4f86f7;
    --navy:#0b1f4d;
    --ink:#2b2f38;
    --muted:#7a8190;
    --rule:#d7dbe3;
    --black:#121417;
  }
  *{box-sizing:border-box;margin:0;padding:0}
  html,body{width:1200px;height:888px;overflow:hidden}
  body{background:var(--bg);position:relative;font-family:"Open Sans",sans-serif;color:var(--ink)}
  .piece{position:absolute;background:var(--paper);box-shadow:0 6px 18px rgba(11,31,77,.15);overflow:hidden}
  .wedge{position:absolute;top:0;left:0}
  .brand{display:flex;align-items:center;gap:8px}
  .brand-dot{width:22px;height:22px;border-radius:50%;background:var(--blue);flex:none}
  .brand-name{font-family:"Montserrat",sans-serif;font-weight:700;color:var(--navy);text-transform:uppercase;letter-spacing:.08em;font-size:13px;line-height:1}
  .tagline{font-family:"Montserrat",sans-serif;font-size:7px;letter-spacing:.2em;text-transform:uppercase;color:var(--blue);margin-top:3px}
  .contact{font-size:7.5px;line-height:1.6;color:var(--muted)}
  .contact b{color:var(--navy);font-weight:600}

  /* Letterhead */
  .letterhead{left:40px;top:40px;width:320px;height:414px}
  .letterhead .side-rule{position:absolute;left:24px;top:96px;width:2px;height:250px;background:var(--blue)}
  .letterhead .brand{position:absolute;left:36px;top:40px}
  .letterhead .body{position:absolute;left:40px;top:104px;right:30px;font-size:7.5px;line-height:1.65}
  .letterhead .body p{margin-bottom:8px}
  .letterhead .sign{font-family:"Montserrat",sans-serif;font-weight:600;color:var(--navy)}
  .letterhead .footer{position:absolute;left:36px;right:30px;bottom:22px;border-top:1px solid var(--rule);padding-top:8px;display:flex;justify-content:space-between}

  /* Fax */
  .fax{left:390px;top:40px;width:320px;height:414px}
  .fax .brand{position:absolute;left:36px;top:40px}
  .fax .fax-title{position:absolute;right:26px;top:38px;font-family:"Montserrat",sans-serif;font-weight:700;font-size:22px;letter-spacing:.15em;color:var(--navy)}
  .fax table{position:absolute;left:36px;right:26px;top:110px;width:calc(100% - 62px);border-collapse:collapse;font-size:8px}
  .fax td{border-bottom:1px solid var(--rule);padding:9px 0;color:var(--navy);font-weight:600}
  .fax td+td{width:75%}
  .fax .checks{position:absolute;left:36px;top:290px;display:flex;gap:18px;font-size:8px;color:var(--muted)}
  .fax .checks span::before{content:"";display:inline-block;width:8px;height:8px;border:1px solid var(--blue);margin-right:4px;vertical-align:-1px}
  .fax .footer{position:absolute;left:36px;right:26px;bottom:22px;border-top:1px solid var(--rule);padding-top:8px;display:flex;justify-content:space-between}

  /* Envelope */
  .envelope{left:40px;top:494px;width:680px;height:295px}
  .envelope .brand{position:absolute;left:40px;top:44px}
  .envelope .return{position:absolute;left:70px;top:82px}
  .envelope .address-lines{position:absolute;left:330px;top:170px;width:240px}
  .envelope .address-lines i{display:block;height:1px;background:var(--rule);margin-bottom:18px}
  .envelope .base-band{position:absolute;left:0;right:0;bottom:0;height:8px;background:linear-gradient(90deg,var(--navy),var(--blue),var(--blue-light))}

  /* Business cards */
  .card{width:380px;height:217px}
  .card-front{left:760px;top:40px}
  .card-front .brand{position:absolute;left:26px;top:30px}
  .card-front .person{position:absolute;left:26px;top:104px}
  .card-front .person-name{font-family:"Montserrat",sans-serif;font-weight:700;font-size:14px;color:var(--navy)}
  .card-front .person-role{font-size:8px;color:var(--blue);letter-spacing:.12em;text-transform:uppercase;margin-top:2px}
  .card-front .contact{position:absolute;right:24px;bottom:22px;text-align:right}
  .card-front .edge{position:absolute;right:0;top:0;bottom:0;width:6px;background:var(--blue)}

  .card-back{left:760px;top:287px;background:linear-gradient(135deg,var(--blue-light),var(--blue) 45%,var(--navy));display:flex;align-items:center;justify-content:center}
  .card-back .brand-dot{background:#fff}
  .card-back .brand-name,.card-back .tagline{color:#fff}
  .card-back .url{position:absolute;bottom:20px;width:100%;text-align:center;font-size:8px;color:#fff;letter-spacing:.15em}

  .card-dark{left:760px;top:534px;background:var(--black);display:flex;align-items:center;justify-content:center}
  .card-dark .brand-name{color:#fff}
  .card-dark .tagline{color:var(--blue-light)}
  .card-dark .corner{position:absolute;left:0;bottom:0;width:100%;height:6px;background:var(--blue)}
</style>
</head>
<body>

<section class="piece letterhead">
  <svg class="wedge" width="120" height="26" viewBox="0 0 120 26"><defs><linearGradient id="g1" x1="0" x2="1"><stop offset="0" stop-color="#0b1f4d"/><stop offset="1" stop-color="#4f86f7"/></linearGradient></defs><polygon points="0,0 120,0 96,26 0,26" fill="url(#g1)"/></svg>
  <div class="brand">
    <span class="brand-dot"></span>
    <div><div class="brand-name">Daniel Whitfield</div><div class="tagline">Marketing Strategist</div></div>
  </div>
  <div class="side-rule"></div>
  <div class="body">
    <p>Client Name<br>Company Address</p>
    <p>Dear Client,</p>
    <p>Thank you for the opportunity to share our plan for your next season of growth and outreach.</p>
    <p>We will review your goals, map the audience, and deliver a clear schedule of campaigns.</p>
    <p>Sincerely,</p>
    <p class="sign">Daniel Whitfield</p>
  </div>
  <div class="footer contact">
    <div>4518 Harwick Crescent<br>Mississauga, Ontario, L4T 3K8</div>
    <div style="text-align:right">danielwhitfield@vellorahaus.com<br><b>www.vellorahaus.com</b></div>
  </div>
</section>

<section class="piece fax">
  <svg class="wedge" width="120" height="26" viewBox="0 0 120 26"><defs><linearGradient id="g2" x1="0" x2="1"><stop offset="0" stop-color="#0b1f4d"/><stop offset="1" stop-color="#4f86f7"/></linearGradient></defs><polygon points="0,0 120,0 96,26 0,26" fill="url(#g2)"/></svg>
  <div class="brand">
    <span class="brand-dot"></span>
    <div><div class="brand-name">Daniel Whitfield</div><div class="tagline">Marketing Strategist</div></div>
  </div>
  <div class="fax-title">FAX</div>
  <table>
    <tr><td>To:</td><td></td></tr>
    <tr><td>From:</td><td></td></tr>
    <tr><td>Date:</td><td></td></tr>
    <tr><td>Pages:</td><td></td></tr>
    <tr><td>Re:</td><td></td></tr>
  </table>
  <div class="checks"><span>Urgent</span><span>Review</span><span>Reply</span></div>
  <div class="footer contact">
    <div>4518 Harwick Crescent<br>Mississauga, Ontario, L4T 3K8</div>
    <div style="text-align:right">danielwhitfield@vellorahaus.com<br><b>www.vellorahaus.com</b></div>
  </div>
</section>

<section class="piece envelope">
  <svg class="wedge" width="260" height="150" viewBox="0 0 260 150"><defs><linearGradient id="g3" x1="0" y1="0" x2="1" y2="1"><stop offset="0" stop-color="#4f86f7" stop-opacity=".35"/><stop offset="1" stop-color="#4f86f7" stop-opacity="0"/></linearGradient></defs><polygon points="0,0 260,0 0,150" fill="url(#g3)"/></svg>
  <div class="brand">
    <span class="brand-dot"></span>
    <div><div class="brand-name">Daniel Whitfield</div><div class="tagline">Marketing Strategist</div></div>
  </div>
  <div class="return contact">4518 Harwick Crescent<br>Mississauga, Ontario, L4T 3K8<br><b>www.vellorahaus.com</b></div>
  <div class="address-lines"><i></i><i></i><i></i></div>
  <div class="base-band"></div>
</section>

<section class="piece card card-front">
  <div class="brand">
    <span class="brand-dot"></span>
    <div><div class="brand-name">Daniel Whitfield</div><div class="tagline">Marketing Strategist</div></div>
  </div>
  <div class="person">
    <div class="person-name">Daniel Whitfield</div>
    <div class="person-role">Marketing Strategist</div>
  </div>
  <div class="contact">4518 Harwick Crescent<br>Mississauga, Ontario, L4T 3K8<br>danielwhitfield@vellorahaus.com<br><b>www.vellorahaus.com</b></div>
  <div class="edge"></div>
</section>

<section class="piece card card-back">
  <div class="brand">
    <span class="brand-dot"></span>
    <div><div class="brand-name">Daniel Whitfield</div><div class="tagline">Marketing Strategist</div></div>
  </div>
  <div class="url">www.vellorahaus.com</div>
</section>

<section class="piece card card-dark">
  <div class="brand">
    <span class="brand-dot"></span>
    <div><div class="brand-name">Daniel Whitfield</div><div class="tagline">Marketing Strategist</div></div>
  </div>
  <div class="corner"></div>
</section>

</body>
</html>
```